Whimsical Aquaculture Farm Packaging Logo

Aquaculture farm in Rhode Island growing hard shell clams (known locally as "quahogs") needs a fun/whimsical (but not silly) label to put on boxes for its "Yuletide Harvest." The "Yuletide Harvest" is actually candy to be given out to friends. The name of the farm is "Perrin Aquaculture Farm."

Boxes are roughly 8x10 so label should fit within those dimensions.

Requirements:
1) Include "Perrin Aquaculture Farm" on the label (it is OK to de-emphasize 'aquaculture' in the type).
2) Include "Yuletide Harvest" (should be more prominent than #1)
3) Do NOT include the year.

Picture of a quahog attached.

Target Market(s)

Existing customers who know us and will get a laugh or chuckle from the playful "Yuletide Harvest" candy.

Industry/Entity Type

Farm

Font styles to use
Serif
Decorative

Colors
33a6d7
85cae6
0892cd
0455a3
3176b5
85acd3

Requirements
Must have
• Should have blue in it (because aquaculture is farming in the ocean).
Should not have
• A date.

```html
<!DOCTYPE html>
<html lang="en">
<head>
<meta charset="utf-8">
<title>Perrin Aquaculture Farm – Yuletide Harvest Label</title>
<link rel="stylesheet" href="https://fonts.googleapis.com/css2?family=Quicksand:wght@500&display=swap">
<style>
  :root {
    --page: #ffffff;
    --sky: #85cae6;
    --aqua: #33a6d7;
    --ocean: #0892cd;
    --deep: #0455a3;
    --steel: #3176b5;
    --mist: #85acd3;
    --field-top: #0f4c9c;
    --field-mid: #1a63b4;
    --ribbon: #1a7cc8;
    --band-core: #1b4fa2;
    --band-edge: #241d5c;
    --ink: #ffffff;
  }
  * { margin: 0; padding: 0; box-sizing: border-box; }
  html, body { width: 1200px; height: 1000px; overflow: hidden; background: var(--page); }
  .canvas { position: relative; width: 1200px; height: 1000px; }
  .label { position: absolute; left: 292px; top: 85px; width: 638px; height: 802px; overflow: hidden; }
  .label-art { position: absolute; inset: 0; width: 100%; height: 100%; display: block; }
  .brand, .headline {
    position: absolute; left: 0; width: 100%;
    text-align: center; color: var(--ink);
    font-family: "Quicksand", sans-serif; font-weight: 500;
  }
  .brand { top: 112px; }
  .brand-line { display: block; line-height: 1; }
  .brand-top { font-size: 40px; letter-spacing: 0.45em; padding-left: 0.45em; }
  .brand-main { font-size: 64px; margin-top: 14px; }
  .brand-bottom { font-size: 32px; letter-spacing: 0.45em; padding-left: 0.45em; margin-top: 16px; }
  .headline { top: 440px; text-transform: uppercase; }
  .headline-line { display: block; line-height: 1; }
  .headline-first { font-size: 84px; letter-spacing: 0.03em; }
  .headline-second { font-size: 76px; letter-spacing: 0.03em; margin-top: 10px; }
</style>
</head>
<body>
<main class="canvas">
  <section class="label">
    <svg class="label-art" viewBox="0 0 638 802">
      <defs>
        <linearGradient id="field-fill" x1="0" y1="0" x2="0" y2="1">
          <stop offset="0" stop-color="var(--field-top)"/>
          <stop offset="1" stop-color="var(--field-mid)"/>
        </linearGradient>
        <radialGradient id="band-fill" cx="0.5" cy="0.5" r="0.6">
          <stop offset="0" stop-color="var(--band-core)"/>
          <stop offset="1" stop-color="var(--band-edge)"/>
        </radialGradient>
        <linearGradient id="edge-fill" x1="0" y1="0" x2="1" y2="0">
          <stop offset="0" stop-color="var(--sky)"/>
          <stop offset="0.5" stop-color="var(--ocean)"/>
          <stop offset="1" stop-color="var(--mist)"/>
        </linearGradient>
        <linearGradient id="flourish-left" x1="0" y1="0" x2="1" y2="0">
          <stop offset="0" stop-color="#5a5a98" stop-opacity="0.55"/>
          <stop offset="1" stop-color="#5a5a98" stop-opacity="0"/>
        </linearGradient>
        <linearGradient id="flourish-right" x1="1" y1="0" x2="0" y2="0">
          <stop offset="0" stop-color="#5a5a98" stop-opacity="0.55"/>
          <stop offset="1" stop-color="#5a5a98" stop-opacity="0"/>
        </linearGradient>
      </defs>

      <rect class="edge-top" x="0" y="0" width="638" height="95" fill="url(#edge-fill)"
            role="img" aria-label="Blue striped pattern border at the top of the label"/>
      <rect class="edge-bottom" x="0" y="640" width="638" height="162" fill="url(#edge-fill)"
            role="img" aria-label="Blue striped pattern border at the bottom of the label"/>

      <rect class="field" x="0" y="90" width="638" height="300" fill="url(#field-fill)"/>

      <path class="ribbon-top" d="M0,322 Q319,432 638,322 L638,372 Q319,462 0,372 Z" fill="var(--ribbon)"/>
      <path class="ribbon-bottom" d="M0,700 Q319,600 638,700 L638,760 Q319,650 0,760 Z" fill="var(--aqua)" fill-opacity="0.7"/>

      <path class="title-band" d="M0,368 Q319,455 638,368 L638,716 Q319,620 0,716 Z" fill="url(#band-fill)"/>

      <path d="M0,372 Q90,396 190,410 L190,690 Q90,696 0,712 Z" fill="url(#flourish-left)"
            role="img" aria-label="Curling winter vine flourishes on the left of the title band"/>
      <path d="M638,372 Q548,396 448,410 L448,690 Q548,696 638,712 Z" fill="url(#flourish-right)"
            role="img" aria-label="Curling winter vine flourishes on the right of the title band"/>
    </svg>

    <h2 class="brand">
      <span class="brand-line brand-top">PERRIN</span>
      <span class="brand-line brand-main">Aquaculture</span>
      <span class="brand-line brand-bottom">FARM</span>
    </h2>

    <h1 class="headline">
      <span class="headline-line headline-first">Yuletide</span>
      <span class="headline-line headline-second">Harvest</span>
    </h1>
  </section>
</main>
</body>
</html>
```